Adult Coloring Book Cover Design

We need a cover created for our New Coloring book.
The title needs to be clear and visible on the front of book. Preferable easy to read when the cover is minimized to about 2 inches on screen. The Full title of the book is:
Quiet Meadow Coloring Book: The Gentle Grownup Coloring Book for Her Patient Wanderers

This is a Religious Based coloring book. Attached are some images from inside the book, feel free to add them to the cover design. We like color!
Looking for something that is attention grabbing but not too over the top.
front cover is 8.5in width and 11in length. I will need all PSD files in order to make any necessary changes once awarded.

```html
<!DOCTYPE html>
<html lang="en">
<head>
<meta charset="utf-8">
<title>Quiet Meadow Coloring Book – Front Cover</title>
<link rel="stylesheet" href="https://fonts.googleapis.com/css2?family=Oswald:wght@600&family=Lato:wght@700&display=swap">
<style>
  :root {
    --stage: #f4f2ee;
    --leather-light: #80653f;
    --leather-dark: #5a4225;
    --frame-ink: #1c140b;
    --frame-band: #2a1e11;
    --title-top: #eaf0a0;
    --title-bottom: #c8df78;
    --rule: #c98f78;
    --subtitle: #ffffff;
    --art-mint: #b9eab3;
    --art-pink: #f3a6c6;
    --art-blue: #7fb5e8;
    --art-gold: #f1e27a;
    --art-shadow: #1f2b1e;
  }
  html, body {
    margin: 0;
    width: 755px;
    height: 1200px;
    overflow: hidden;
    background: var(--stage);
  }
  .cover {
    position: absolute;
    left: 20px;
    top: 137px;
    width: 715px;
    height: 925px;
    background: radial-gradient(ellipse at 50% 45%, var(--leather-light), var(--leather-dark));
    box-shadow: 0 6px 18px rgba(0,0,0,.25);
    overflow: hidden;
  }
  .frame {
    position: absolute;
    inset: 0;
  }
  .title {
    position: absolute;
    left: 0;
    right: 0;
    top: 158px;
    margin: 0;
    text-align: center;
    font-family: "Oswald", sans-serif;
    font-weight: 600;
    font-size: 62px;
    line-height: 74px;
    letter-spacing: 1px;
    text-transform: uppercase;
    background: linear-gradient(180deg, var(--title-top), var(--title-bottom));
    -webkit-background-clip: text;
    background-clip: text;
    color: transparent;
    filter: drop-shadow(2px 3px 0 rgba(0,0,0,.55));
  }
  .title span { display: block; }
  .rule {
    position: absolute;
    left: 150px;
    width: 415px;
    height: 2px;
    background: linear-gradient(90deg, transparent, var(--rule) 15%, var(--rule) 85%, transparent);
  }
  .rule--above-title { top: 150px; }
  .rule--below-title { top: 322px; }
  .rule--above-subtitle { top: 734px; }
  .rule--below-subtitle { top: 818px; }
  .cover-art {
    position: absolute;
    left: 198px;
    top: 332px;
    width: 320px;
    height: 398px;
    border-radius: 18px;
    background:
      radial-gradient(circle at 50% 20%, var(--art-gold) 0 18%, transparent 34%),
      radial-gradient(circle at 50% 82%, var(--art-blue) 0 20%, transparent 36%),
      radial-gradient(circle at 50% 38%, var(--art-pink) 0 12%, transparent 28%),
      linear-gradient(180deg, var(--art-mint), #9fd79d 55%, var(--art-shadow));
  }
  .subtitle {
    position: absolute;
    left: 0;
    right: 0;
    top: 744px;
    margin: 0;
    text-align: center;
    font-family: "Lato", sans-serif;
    font-weight: 700;
    font-size: 22px;
    line-height: 30px;
    color: var(--subtitle);
    text-shadow: 1px 1px 2px rgba(0,0,0,.6);
  }
</style>
</head>
<body>
  <main class="cover">
    <svg class="frame" width="715" height="925" viewBox="0 0 715 925" aria-hidden="true">
      <rect x="14" y="14" width="687" height="897" fill="none" stroke="var(--frame-band)" stroke-width="14"/>
      <rect x="30" y="30" width="655" height="865" fill="none" stroke="var(--frame-ink)" stroke-width="2"/>
      <rect x="46" y="46" width="623" height="833" fill="none" stroke="var(--frame-band)" stroke-width="10" opacity=".8"/>
      <rect x="60" y="60" width="595" height="805" fill="none" stroke="var(--frame-ink)" stroke-width="3"/>
      <rect x="68" y="68" width="579" height="789" fill="none" stroke="var(--frame-ink)" stroke-width="1"/>
    </svg>
    <svg class="frame" width="715" height="925" viewBox="0 0 715 925">
      <g fill="var(--frame-band)" opacity=".85">
        <path role="img" aria-label="Ornamental corner, top left" d="M68 68 H200 L68 200 Z"/>
        <path role="img" aria-label="Ornamental corner, top right" d="M647 68 H515 L647 200 Z"/>
        <path role="img" aria-label="Ornamental corner, bottom left" d="M68 857 H200 L68 725 Z"/>
        <path role="img" aria-label="Ornamental corner, bottom right" d="M647 857 H515 L647 725 Z"/>
        <rect role="img" aria-label="Small ornament, top centre" x="327" y="72" width="60" height="22" rx="8"/>
        <rect role="img" aria-label="Small ornament, bottom centre" x="327" y="831" width="60" height="22" rx="8"/>
      </g>
    </svg>

    <div class="rule rule--above-title"></div>
    <h1 class="title"><span>Quiet Meadow</span><span>Coloring Book</span></h1>
    <div class="rule rule--below-title"></div>

    <div class="cover-art" role="img" aria-label="Featured colored page from the book in mint, yellow, pink and blue tones"></div>

    <div class="rule rule--above-subtitle"></div>
    <p class="subtitle">The Gentle Grownup Coloring Book<br>for Her Patient Wanderers</p>
    <div class="rule rule--below-subtitle"></div>
  </main>
</body>
</html>
```